U.S. based testing, inspection, and certification (TIC) company needs a new social media design.

We need a social media design primarily for LinkedIn 1200x1200px for our U.S. based company with international capabilities for performing dozens if not hundreds of testing, inspection, and certification (TIC) services. Our primary services include calibration, chemical analysis, consulting engineering, environmental simulation, forensic engineering, materials testing, mechanical testing, and nondestructive testing. Industries we serve are aerospace/aviation, automotive, chemical, commercial properties, construction, consumer products, defense, energy storage, healthcare, insurance/legal, life science, manufacturing, oil & gas, power generation, pulp & paper, and telecommunications. https://veltrolabs.example/

Guideline hex colors (primary, secondary): #29aae2, #0b1f3b

The final design should communicate:
1. Trust, Integrity, and Independence
2. Technical Expertise and Accuracy
3. Efficiency and Speed
4. Value-Added Partnership

We previously used a hexagon design that we would like to part ways from; hexagon examples and KRV logos uploaded.

```html
<!DOCTYPE html>
<html lang="en">
<head>
<meta charset="utf-8">
<title>KRV – Social Media Posts</title>
<link href="https://fonts.googleapis.com/css2?family=Montserrat:wght@500;700&family=Arimo:wght@700&display=swap" rel="stylesheet">
<style>
  :root{
    --primary:#29aae2;
    --navy:#0b1f3b;
    --white:#ffffff;
    --sky-pale:#d3ebfd;
    --sky-light:#bde2fc;
    --cyan-soft:#6fcdf8;
    --blue-top:#00b8f6;
    --blue-mid:#0a8ff0;
    --blue-deep:#0a5be6;
    --photo-grey:#9aa4ad;
  }
  *{margin:0;padding:0;box-sizing:border-box}
  html,body{width:1200px;height:1129px;overflow:hidden;background:var(--white)}
  .stage{position:absolute;left:0;top:0;width:1988px;height:1870px;transform:scale(0.60362);transform-origin:0 0}
  .post{position:absolute;width:772px;height:772px;overflow:hidden}
  .post--aviation{left:608px;top:89px}
  .post--liability{left:183px;top:941px}
  .post--materials{left:1033px;top:941px}
  .post-bg{position:absolute;inset:0;width:772px;height:772px}
  .brand{position:absolute;right:42px;top:44px;display:flex;align-items:center;gap:12px;
    font-family:"Montserrat",sans-serif;font-weight:700;font-size:54px;letter-spacing:4px;line-height:1}
  .brand__mark{width:22px;height:22px}
  .brand--blue{color:var(--primary)}
  .brand--blue .brand__mark{background:var(--primary)}
  .brand--white{color:var(--white)}
  .brand--white .brand__mark{background:var(--white)}
  .headline{position:absolute;font-family:"Montserrat",sans-serif;font-weight:700;color:var(--white)}
  .body-copy{position:absolute;font-family:"Arimo",Arial,sans-serif;font-weight:700}
  .body-copy--navy{color:var(--navy)}
  .body-copy--white{color:var(--white)}
  .line{display:block;white-space:nowrap}
  .line--just{text-align:justify;text-align-last:justify}
  .url{position:absolute;right:41px;bottom:38px;font-family:"Montserrat",sans-serif;font-weight:500;font-size:24px;color:var(--white);letter-spacing:.3px}
  .photo{position:absolute}

  .post--aviation .headline{left:41px;top:280px;font-size:50px;line-height:65px}
  .post--aviation .body-copy{left:39px;top:494px;width:630px;font-size:29px;line-height:37px}

  .post--liability .headline{left:0;width:772px;top:150px;font-size:57px;text-align:center;line-height:63px}
  .post--liability .subhead{position:absolute;left:124px;top:500px;font-family:"Montserrat",sans-serif;font-weight:700;font-size:34px;color:var(--white);white-space:nowrap}
  .post--liability .body-copy{left:123px;top:551px;width:525px;font-size:27px;line-height:34px}

  .post--materials .body-copy{font-size:23.5px;line-height:28px}
  .copy--aero{left:400px;top:152px;width:292px}
  .copy--quality{left:112px;top:364px;width:250px}
  .copy--analysis{left:400px;top:510px}
</style>
</head>
<body>
<div class="stage">

  <section class="post post--aviation">
    <svg class="post-bg" viewBox="0 0 772 772" aria-hidden="true">
      <defs>
        <linearGradient id="avBlue" x1="0" y1="0" x2="0" y2="1">
          <stop offset="0" stop-color="var(--blue-top)"/>
          <stop offset="0.55" stop-color="var(--blue-mid)"/>
          <stop offset="1" stop-color="var(--blue-deep)"/>
        </linearGradient>
        <linearGradient id="avCyan" x1="0" y1="0" x2="0" y2="1">
          <stop offset="0" stop-color="#8fd6fa"/>
          <stop offset="1" stop-color="var(--cyan-soft)"/>
        </linearGradient>
      </defs>
      <rect width="772" height="772" fill="var(--sky-light)"/>
      <polygon points="300,146 430,0 772,0 772,145" fill="var(--sky-pale)"/>
      <polygon points="0,146 300,146 772,678 772,772 405,772 0,330" fill="url(#avBlue)"/>
      <polygon points="0,330 405,772 0,772" fill="url(#avCyan)"/>
      <polygon points="225,772 405,772 300,655" fill="#7fd2f9" opacity=".6"/>
    </svg>
    <svg class="photo" style="left:82px;top:128px" width="630" height="160" viewBox="0 0 630 160" role="img" aria-label="Photo of a wide-body passenger jet in flight with landing gear down">
      <defs>
        <linearGradient id="avPhoto" x1="0" y1="0" x2="1" y2="0">
          <stop offset="0" stop-color="#c9d3de" stop-opacity=".75"/>
          <stop offset="1" stop-color="#eef2f6" stop-opacity=".85"/>
        </linearGradient>
      </defs>
      <rect x="0" y="0" width="630" height="160" rx="16" fill="url(#avPhoto)"/>
    </svg>
    <div class="brand brand--blue"><span class="brand__mark"></span>KRV</div>
    <h1 class="headline">We Take You<br>from Confidence<br>to Certainty</h1>
    <p class="body-copy body-copy--navy">
      <span class="line line--just">Our calibration avionics experts offers LCD</span>
      <span class="line line--just">display upgrades for Avtrex GSX-800 and</span>
      <span class="line">GSX-800-2 ground station simulators.</span>
    </p>
    <div class="url">https://veltrolabs.example</div>
  </section>

  <section class="post post--liability">
    <svg class="post-bg" viewBox="0 0 772 772" aria-hidden="true">
      <defs>
        <linearGradient id="liBlue" x1="0" y1="0" x2="0" y2="1">
          <stop offset="0" stop-color="var(--blue-top)"/>
          <stop offset="0.55" stop-color="var(--blue-mid)"/>
          <stop offset="1" stop-color="var(--blue-deep)"/>
        </linearGradient>
        <linearGradient id="liCyan" x1="0" y1="0" x2="0" y2="1">
          <stop offset="0" stop-color="#7cc3fa"/>
          <stop offset="1" stop-color="var(--cyan-soft)"/>
        </linearGradient>
      </defs>
      <rect width="772" height="772" fill="url(#liBlue)"/>
      <polygon points="453,0 772,0 772,140 690,225" fill="var(--sky-pale)"/>
      <polygon points="690,225 772,140 772,320" fill="var(--sky-light)"/>
      <polygon points="0,365 410,772 0,772" fill="url(#liCyan)"/>
      <polygon points="0,460 100,365 300,565" fill="#8ccbfb" opacity=".45"/>
    </svg>
    <div class="brand brand--blue"><span class="brand__mark"></span>KRV</div>
    <h1 class="headline">Same Standards.<br>Better Methods.</h1>
    <svg class="photo" style="left:0;top:297px" width="772" height="178" viewBox="0 0 772 178">
      <polygon points="200,0 332,0 272,178 132,178" fill="#4d5b66" role="img" aria-label="Photo of a car dashboard seen through a rain-covered windshield"/>
      <polygon points="357,0 485,0 417,178 285,178" fill="#8a7a5e" role="img" aria-label="Photo of a construction worker in a hard hat and safety vest inspecting a surface"/>
      <polygon points="509,0 639,0 567,178 437,178" fill="var(--photo-grey)" role="img" aria-label="Photo of a damaged industrial metal component with drilled ports"/>
    </svg>
    <h2 class="subhead">Subrogation Product Liability</h2>
    <p class="body-copy body-copy--navy">
      <span class="line line--just">Our experts perform product failure</span>
      <span class="line line--just">assessments to determine if a loss is a</span>
      <span class="line line--just">result of poor design, a manufacuring</span>
      <span class="line">defect or operator error.</span>
    </p>
    <div class="url">https://veltrolabs.example</div>
  </section>

  <section class="post post--materials">
    <svg class="post-bg" viewBox="0 0 772 772" aria-hidden="true">
      <defs>
        <linearGradient id="maBlue" x1="0" y1="0" x2="0" y2="1">
          <stop offset="0" stop-color="var(--blue-top)"/>
          <stop offset="0.5" stop-color="var(--blue-mid)"/>
          <stop offset="1" stop-color="var(--blue-deep)"/>
        </linearGradient>
      </defs>
      <rect width="772" height="772" fill="url(#maBlue)"/>
      <polygon points="0,0 123,0 0,65" fill="var(--sky-light)"/>
      <polygon points="648,772 772,772 772,705" fill="var(--sky-light)"/>
      <polygon points="0,102 297,102 400,296 0,296" fill="#a7b0b8" role="img" aria-label="Photo of a large aerospace metal structure under assembly"/>
      <polygon points="405,303 772,303 772,497 505,497" fill="#d3d8dd" role="img" aria-label="Photo of laboratory staff in white coats working at analytical instruments"/>
      <polygon points="0,502 297,502 400,696 0,696" fill="#c4ccd4" role="img" aria-label="Close-up photo of a microscope objective lens above a sample slide"/>
    </svg>
    <div class="brand brand--white"><span class="brand__mark"></span>KRV</div>
    <p class="body-copy body-copy--white copy--aero">
      <span class="line line--just">Materials and analytical</span>
      <span class="line">testing for aerospace.</span>
    </p>
    <p class="body-copy body-copy--white copy--quality">
      <span class="line line--just">We provide material</span>
      <span class="line line--just">verification and quality</span>
      <span class="line">control.</span>
    </p>
    <p class="body-copy body-copy--white copy--analysis">
      <span class="line">Our advance analytical</span>
      <span class="line">services include sanning</span>
      <span class="line">electron microscopy,</span>
      <span class="line">energy-dispersive x-ray</span>
      <span class="line">spectroscopy, and x-ray</span>
      <span class="line">diffraction.</span>
    </p>
    <div class="url">https://veltrolabs.example</div>
  </section>

</div>
</body>
</html>
```